Need simple and modern looking business card with all my information on one side and logo on the other side
Info :
Company name - VELMAR CONSTRUCTION LLC
Company addres- 418 harbor 87th. Dunmoor park ny 10352
Email- velmarllc@tridomail.Com
Company phone number 555-318-6094
Cell number- 555-742-0583
Web site - velmarllc.Com
My name Gerald tomasino

Target Market(s)

Construction , home improvement, remodeling

Industry/Entity Type

Construction

Contact Information for Business Card

It has to be moder but at the same time simple

Font styles to use
Sans Serif

Colors
0255a3
ffffff
000000
f78f20
b1b1b1
9d9d9d
1b1b1b
33a6d7
ec1f27

Requirements
Must have
• My logo on one side maybe with a some kind of background on the other side all my information
Nice to have
• Some kind of background pictures provided by you .PLEASE HAVE ACCOUNT WITH PIXELVAULT WILL NOT PAY ANY EXTRA FEES .
Should not have
• Any kind of hamer, nails,screws, helmets itp. Please do not copy the other designs come up with something new.

```html
<!DOCTYPE html>
<html lang="en">
<head>
<meta charset="utf-8">
<title>Velmar Construction LLC – Business Card</title>
<link href="https://fonts.googleapis.com/css2?family=Open+Sans:wght@400;600;700&display=swap" rel="stylesheet">
<style>
  :root {
    --orange: #f78f20;
    --ink: #1b1b1b;
    --black: #000000;
    --white: #ffffff;
    --grey-light: #b1b1b1;
    --grey: #9d9d9d;
    --blue: #0255a3;
    --sky: #33a6d7;
    --backdrop: #e7e5e1;
  }
  * { box-sizing: border-box; margin: 0; padding: 0; }
  html, body { width: 1200px; height: 780px; overflow: hidden; }
  body {
    background: var(--backdrop);
    font-family: "Open Sans", Arial, sans-serif;
    display: flex;
    align-items: center;
    justify-content: center;
    gap: 40px;
  }
  .card {
    position: relative;
    width: 540px;
    height: 310px;
    background: var(--white);
    box-shadow: 0 6px 18px rgba(0,0,0,.18);
    overflow: hidden;
  }
  .card-art { position: absolute; inset: 0; width: 100%; height: 100%; }

  /* front: contact side */
  .brand { position: absolute; left: 34px; top: 70px; color: var(--ink); font-weight: 700; line-height: 1; }
  .brand-name { font-size: 46px; letter-spacing: 2px; }
  .brand-sub { font-size: 14px; letter-spacing: 2.4px; margin-top: 4px; }
  .holder-name {
    position: absolute; left: 160px; top: 160px;
    color: var(--orange); font-weight: 700; font-size: 18px;
  }
  .contact {
    position: absolute; left: 330px; top: 108px;
    color: var(--ink); font-size: 12.5px; line-height: 1.45;
    list-style: none;
  }
  .contact li { display: flex; align-items: center; gap: 7px; }
  .contact .address { display: block; margin-bottom: 4px; padding-left: 22px; }
  .icon { width: 15px; height: 15px; flex: none; }

  /* back: logo side */
  .card-back { background: linear-gradient(135deg, #f7f7f7 0%, #e4e4e4 100%); }
  .back-photo {
    position: absolute; left: 60px; top: 0; width: 420px; height: 310px;
    background: linear-gradient(180deg, rgba(177,177,177,.18), rgba(157,157,157,.08));
  }
  .back-brand { position: absolute; left: 52px; top: 160px; color: var(--ink); font-weight: 700; line-height: 1; display: flex; align-items: center; gap: 12px; }
  .back-brand-mark { width: 16px; height: 16px; background: var(--orange); }
  .back-brand .brand-name { font-size: 52px; }
  .back-brand .brand-sub { font-size: 15px; }
  .website {
    position: absolute; right: 26px; bottom: 24px;
    color: var(--ink); font-weight: 600; font-size: 13px;
  }
</style>
</head>
<body>

<section class="card card-front">
  <svg class="card-art" viewBox="0 0 540 310" aria-hidden="false">
    <path d="M230,0 H540 V96 C430,104 320,80 230,0 Z" fill="url(#skyTone)" role="img" aria-label="Photo of tower cranes over a city construction site"/>
    <path d="M230,0 C320,80 430,104 540,96" fill="none" stroke="var(--orange)" stroke-width="7"/>
    <path d="M0,220 C120,178 270,196 390,310 H0 Z" fill="url(#siteTone)" role="img" aria-label="Photo of workers in safety vests among steel rebar on site"/>
    <path d="M0,220 C120,178 270,196 390,310" fill="none" stroke="var(--orange)" stroke-width="7"/>
    <defs>
      <linearGradient id="skyTone" x1="0" y1="0" x2="1" y2="1">
        <stop offset="0" stop-color="#b9cde0"/>
        <stop offset="1" stop-color="#cbbfa8"/>
      </linearGradient>
      <linearGradient id="siteTone" x1="0" y1="0" x2="1" y2="1">
        <stop offset="0" stop-color="#c9c2b6"/>
        <stop offset="1" stop-color="#6d6a66"/>
      </linearGradient>
    </defs>
  </svg>

  <div class="brand">
    <div class="brand-name">VELMAR</div>
    <div class="brand-sub">CONSTRUCTION LLC</div>
  </div>

  <p class="holder-name">Gerald tomasino</p>

  <ul class="contact">
    <li class="address">418 harbor 87th.<br>Dunmoor park ny 10352</li>
    <li>
      <svg class="icon" viewBox="0 0 16 16"><rect width="16" height="16" fill="var(--orange)"/><path d="M4 5c1-1 2-1 2 0l1 2-1 1c.5 1 1 1.5 2 2l1-1 2 1c1 0 1 1 0 2-3 1-8-4-7-7z" fill="var(--white)"/></svg>
      555-318-6094
    </li>
    <li>
      <svg class="icon" viewBox="0 0 16 16"><rect width="16" height="16" fill="var(--orange)"/><rect x="5" y="3" width="6" height="10" rx="1" fill="none" stroke="var(--white)" stroke-width="1.3"/><circle cx="8" cy="11" r=".8" fill="var(--white)"/></svg>
      555-742-0583
    </li>
    <li>
      <svg class="icon" viewBox="0 0 16 16"><rect width="16" height="16" fill="var(--orange)"/><rect x="3" y="5" width="10" height="7" fill="none" stroke="var(--white)" stroke-width="1.2"/><path d="M3 5l5 4 5-4" fill="none" stroke="var(--white)" stroke-width="1.2"/></svg>
      velmarllc@tridomail.Com
    </li>
  </ul>
</section>

<section class="card card-back">
  <div class="back-photo" role="img" aria-label="Faint photo of a building under construction"></div>
  <div class="back-brand">
    <span class="back-brand-mark"></span>
    <div>
      <div class="brand-name">VELMAR</div>
      <div class="brand-sub">CONSTRUCTION LLC</div>
    </div>
  </div>
  <p class="website">velmarllc.Com</p>
</section>

</body>
</html>
```